Commercial Real Estate Company Needs an Awesome Flyer Design for their Oceanfront Property

We need a 2-page flyer or our Class A Oceanfront Property in Santa Monica, California. Approximately 16,149 square feet of Class A rare oceanfront office space with private balconies will be in available 4th Quarter of 2014. The SPACE has not been on the market for over 20 YEARS!

I attached our Previous 2-page flyer for the 2,353 square feet. We need a new vibrant, modern flyer that will attract Tech, Entertainment, Financial, and Marketing Companies to our building. Also, the 2nd Floor Space Plan is attached.

Also, please check out our website www.verlindeproperty.com. We would like to use the colors of our website and logo to incorporate with the flyer.

I updated the Must Have's on the Listing!

Target Market(s)

Entertainment, Financial, Tech Companies

Industry/Entity Type

Real Estate

Requirements
Must have
• Our Company Logo, Company, Leasing Agents On the First and 2nd Page

Trevor L. Ashdown (310) 555-0142
trev@verlindeproperty.com

Mark Oda (310) 555-0187
mark@verlindeproperty.com

Verlinde Property.
5127 N Harlow Ave, Suite 210
West Hollywood, Ca. 90069
(310) 555-0142
www.verlindeproperty.com

Also, the Front Page should indicate

"Rare Class A Oceanfront Office Space in the heart of Santa Monica"
"2nd Floor Office Space consisting of 16,159 square feet with private balconies."
Nice to have
• Please use description of the office building. You can omit whatever you think is unnecessary

"Bellhaven Court is one of Santa Monica's rare commercial properties that is both strategically located in the city's burgeoning central business district, yet ideally positioned on palm-lined Ocean Ave directly across from the Pacific Ocean. Built in 1987, the 3-story mixed-use commercial and retail property features prestigious retail Tenants such as Kelp Tavu and Dune Kitchen."

"A year-round coastal Mediterranean climate, a highly diverse business sector, and the vibrant, pedestrian-oriented Linden Row Walkway and Harbor Crest Arcade makes this beachside community a highly desirable commercial and retail location."

```html
<!DOCTYPE html>
<html lang="en">
<head>
<meta charset="utf-8">
<title>Bellhaven Court – Oceanfront Office Flyer</title>
<link rel="stylesheet" href="https://fonts.googleapis.com/css2?family=Jura:wght@300;400;600&display=swap">
<style>
  :root{
    --yellow:#e9c31d;
    --yellow-deep:#d2a912;
    --charcoal:#3b3b3b;
    --grey-light:#e6e6e6;
    --grey-mid:#a9a9a9;
    --ink:#2e2e2e;
    --white:#ffffff;
    --stage:#dcd9d3;
  }
  *{margin:0;padding:0;box-sizing:border-box}
  html,body{width:1200px;height:900px;overflow:hidden}
  body{background:var(--stage);font-family:"Jura",sans-serif;color:var(--ink);position:relative}

  .flyer-page{position:absolute;top:100px;width:540px;height:700px;overflow:hidden;
    background:linear-gradient(180deg,var(--grey-light) 0%,#cfcfcf 55%,var(--grey-mid) 100%);
    box-shadow:0 6px 18px rgba(0,0,0,.25)}
  .page-front{left:40px}
  .page-back{left:620px}
  .page-shapes{position:absolute;inset:0;width:540px;height:700px}

  /* front page */
  .hero-photo{position:absolute;left:0;top:60px;width:540px;height:355px;
    background:linear-gradient(180deg,#3f5f9e 0%,#7f97c4 30%,#e4e4e0 55%,#b9b8b0 72%,#4a4d55 100%)}
  .brand-tile{position:absolute;left:170px;top:0;width:92px;height:82px;background:var(--white);
    display:flex;flex-direction:column;align-items:center;justify-content:center;gap:6px}
  .brand-dot{width:22px;height:22px;border-radius:50%;background:var(--ink)}
  .brand-name{font-weight:600;font-size:10px;letter-spacing:1.5px;text-align:center;line-height:1.2;color:var(--ink);text-transform:uppercase}

  .space-facts{position:absolute;right:34px;color:var(--white);font-weight:300;font-size:14px;line-height:1.1;text-align:right}
  .fact-size{top:418px;right:110px}
  .fact-class{top:440px}
  .fact-balcony{top:494px;right:44px}
  .fact-date{top:532px;right:22px}

  .contact-block{position:absolute;left:26px;top:515px;font-size:11.5px;line-height:1.2;color:var(--ink);font-weight:400}
  .contact-block p{margin-bottom:9px}
  .contact-block p:last-child{margin-bottom:0}

  /* back page */
  .photo-reception{position:absolute;left:10px;top:28px;width:180px;height:108px;
    background:linear-gradient(180deg,#d9d3c4 0%,#b89d5e 55%,#8a8676 100%)}
  .photo-elevators{position:absolute;left:10px;top:136px;width:180px;height:104px;
    background:linear-gradient(180deg,#dcdde0 0%,#8f9197 60%,#6b2f33 100%)}
  .plan-panel{position:absolute;left:190px;top:28px;width:170px;height:212px;background:var(--yellow)}
  .plan-drawing{position:absolute;left:12px;top:14px;width:146px;height:175px;background:#d7b21a}
  .photo-balcony{position:absolute;left:360px;top:28px;width:170px;height:212px;
    background:linear-gradient(180deg,#4f79b8 0%,#9fb8d8 45%,#c9c8c2 65%,#4f6b3a 100%)}

  .property-story{position:absolute;font-size:13px;line-height:1.2;color:var(--ink);font-weight:400}
  .story-intro{top:290px;left:40px;width:460px;text-align:center}
  .story-climate{top:395px;right:26px;width:300px;text-align:right}

  .curve-label{font-family:"Jura",sans-serif;fill:var(--white)}
</style>
</head>
<body>

<section class="flyer-page page-front" aria-label="Flyer front page">
  <div class="hero-photo" role="img" aria-label="Photo of the white three-storey Bellhaven Court building with palm trees and ground-floor retail under a blue sky"></div>
  <svg class="page-shapes" viewBox="0 0 540 700" aria-hidden="true">
    <defs>
      <linearGradient id="frontGrey" x1="0" y1="0" x2="0" y2="1">
        <stop offset="0" stop-color="#b5b5b5"/><stop offset="1" stop-color="#8c8c8c"/>
      </linearGradient>
      <path id="frontCurve" d="M6 478 C268 470 450 576 510 700"/>
    </defs>
    <rect x="0" y="0" width="540" height="58" fill="var(--yellow)"/>
    <path d="M0 58 L540 58 L540 60 C380 64 160 70 0 80 Z" fill="#d9d9d9"/>
    <path d="M0 68 C160 64 380 60 540 58 L540 62 C380 66 160 72 0 78 Z" fill="var(--white)"/>
    <path d="M0 410 L540 404 L540 700 L0 700 Z" fill="var(--charcoal)"/>
    <path d="M0 410 L540 404 L540 408 L0 414 Z" fill="#9a9a9a"/>
    <path d="M0 492 C250 486 430 590 490 700 L0 700 Z" fill="url(#frontGrey)"/>
    <path d="M0 448 C280 440 470 560 530 700 L490 700 C430 590 250 486 0 492 Z" fill="var(--yellow)"/>
    <path d="M0 492 C250 486 430 590 490 700 L482 700 C422 596 248 498 0 498 Z" fill="#c8c8c8"/>
    <text class="curve-label" font-size="25" font-weight="300"><textPath href="#frontCurve">in the heart of Santa Monica</textPath></text>
  </svg>
  <div class="brand-tile">
    <span class="brand-dot"></span>
    <span class="brand-name">Verlinde<br>Property</span>
  </div>

  <p class="space-facts fact-size">16,149 square feet</p>
  <p class="space-facts fact-class">Class A rare<br>oceanfront office<br>on 2nd Floor</p>
  <p class="space-facts fact-balcony">with private<br>balconies</p>
  <p class="space-facts fact-date">will be in<br>available<br>4th<br>Quarter<br>of 2014</p>

  <div class="contact-block">
    <p>Trevor L. Ashdown<br>(310) 555-0142<br>trev@verlindeproperty.com</p>
    <p>Mark Oda<br>(310) 555-0187<br>mark@verlindeproperty.com</p>
    <p>Verlinde Property.<br>5127 N Harlow Ave, Suite 210<br>West Hollywood, Ca. 90069<br>(310) 555-0142<br>www.verlindeproperty.com</p>
  </div>
</section>

<section class="flyer-page page-back" aria-label="Flyer back page">
  <div class="photo-reception" role="img" aria-label="Photo of the office reception area with a curved wooden front desk"></div>
  <div class="photo-elevators" role="img" aria-label="Photo of the elevator lobby with grey panels and red carpet"></div>
  <div class="plan-panel">
    <div class="plan-drawing" role="img" aria-label="2nd floor space plan drawing"></div>
  </div>
  <div class="photo-balcony" role="img" aria-label="Photo of a private balcony overlooking palm trees and the ocean"></div>
  <svg class="page-shapes" viewBox="0 0 540 700" aria-hidden="true">
    <defs>
      <linearGradient id="backGrey" x1="0" y1="0" x2="0" y2="1">
        <stop offset="0" stop-color="#bdbdbd"/><stop offset="1" stop-color="#909090"/>
      </linearGradient>
      <path id="backCurve" d="M14 484 C260 474 425 550 535 628"/>
    </defs>
    <path d="M0 230 C180 250 380 225 540 190 L540 262 L0 262 Z" fill="#dcdcdc"/>
    <path d="M0 240 C180 258 380 234 540 200 L540 214 C380 248 180 270 0 252 Z" fill="#b9b9b9"/>
    <path d="M0 252 C180 270 380 248 540 214 L540 240 C380 268 180 282 0 270 Z" fill="var(--grey-light)"/>
    <path d="M0 492 C250 488 420 560 540 640 L540 700 L0 700 Z" fill="url(#backGrey)"/>
    <path d="M0 462 C260 452 430 530 540 610 L540 645 C420 565 250 492 0 494 Z" fill="var(--yellow)"/>
    <path d="M0 494 C250 492 420 565 540 645 L540 652 C418 574 248 500 0 500 Z" fill="#c8c8c8"/>
    <text class="curve-label" font-size="14.5" font-weight="400"><textPath href="#backCurve">The SPACE has not been on the market for over 20 YEARS!</textPath></text>
  </svg>

  <p class="property-story story-intro">Bellhaven Court is one of Santa Monica’s rare commercial properties that is both strategically located in the city’s burgeoning central business district, yet ideally positioned on palm-lined Ocean Ave directly across from the Pacific Ocean. Built in 1987, the 3-story mixed-use commercial and retail property features prestigious retail Tenants such as Kelp Tavu and Dune Kitchen.</p>
  <p class="property-story story-climate">A year-round coastal Mediterranean climate, a highly diverse business sector, and the vibrant, pedestrian-oriented Linden Row Walkway and Harbor Crest Arcade makes this beachside community a highly desirable commercial and retail location</p>

  <div class="contact-block">
    <p>Trevor L. Ashdown<br>(310) 555-0142<br>trev@verlindeproperty.com</p>
    <p>Mark Oda<br>(310) 555-0187<br>mark@verlindeproperty.com</p>
    <p>Verlinde Property.<br>5127 N Harlow Ave, Suite 210<br>West Hollywood, Ca. 90069<br>(310) 555-0142<br>www.verlindeproperty.com</p>
  </div>
</section>

</body>
</html>
```